Fern Lattice Logo, Icons and web design

Looking for a new logo for the Sprout Oracle, and a set of 12-15 icons and color scheme (and a few sample pages) to include some creative, but clean and professional content boxes. The current site is http://www.fernlattice-example.com. We would like to see logo variants - both based on the current design, as well as some new creative options.
Fern Lattice is a SaaS website designed for the green industry participants who want to save trees during construction or other land disturbances (landscape architects, builders/developers, architects, homeowners). It features a patented algorithm to predict tree survival. We also offer the Sprout Oracle to find the best plant for the planting location.

We would like to see a page with embedded video for our promotional and tutorial videos.

Specifically we would to see icons for two services:

Fern Lattice: A root plotting tree survival prediction tool
https://www.fernlattice-example.com/how-bark-keeper-works

Our Sprout Oracle: https://www.fernlattice-example.com/how-sprout-oracle-works
The current site is based on a twitter bootstrap 4.0 template, so this is strongly preferred.

Target Market(s)

Landscape architects, builders and developer as well as municipal tree planning and preservation specialists.

Coding

Coded - Design and coding required

Number of Pages Required

4 page

Font styles to use
Sans Serif

```html
<!DOCTYPE html>
<html lang="en">
<head>
<meta charset="utf-8">
<title>Fern Lattice</title>
<link rel="stylesheet" href="https://fonts.googleapis.com/css2?family=Open+Sans:wght@400;600;700;800&display=swap">
<style>
:root{
  --green:#3d9a2c;
  --green-dark:#2b7a1d;
  --green-light:#7cc35f;
  --ink:#2f2f2f;
  --muted:#6b6b6b;
  --band:#efefef;
  --footer:#2a2a2a;
  --footer-bar:#1f1f1f;
  --white:#ffffff;
}
*{box-sizing:border-box;margin:0;padding:0}
html,body{width:1200px;height:3864px;overflow:hidden}
body{font-family:"Open Sans",Arial,sans-serif;color:var(--ink);background:var(--white);position:relative}
section,header,footer{position:absolute;left:0;width:1200px}
ul{list-style:none}

/* header */
.site-header{top:0;height:160px;background:var(--white);box-shadow:0 2px 6px rgba(0,0,0,.08);z-index:3}
.brand{position:absolute;left:72px;top:22px;display:flex;flex-direction:column;align-items:center}
.brand-mark{width:64px;height:64px;border-radius:50%;background:var(--green)}
.brand-name{margin-top:8px;font-size:22px;font-weight:700;color:var(--green);letter-spacing:1px}
.call-pill{position:absolute;right:90px;top:18px;height:48px;padding:0 22px 0 10px;border-radius:24px;background:var(--white);display:flex;align-items:center;gap:12px;font-size:18px;font-weight:700;color:var(--green)}
.call-icon{width:44px;height:44px;border-radius:50%;background:var(--green);display:flex;align-items:center;justify-content:center}
.main-nav{position:absolute;left:380px;top:112px;display:flex;gap:44px;font-size:15px;font-weight:700;color:var(--ink)}
.main-nav .active{color:var(--green);border-bottom:3px solid var(--green);padding-bottom:6px}

/* hero */
.hero{top:160px;height:780px;overflow:hidden}
.hero-art{position:absolute;inset:0;background:linear-gradient(135deg,#e9ece4 0%,#cfd8c4 35%,#b7c7a5 60%,#e4e1d2 100%)}
.hero-box{position:absolute;left:288px;top:160px;width:624px;height:300px;background:rgba(30,30,30,.72);text-align:center;color:var(--white);padding-top:34px}
.hero-box h1{font-size:44px;font-weight:700;letter-spacing:2px}
.hero-box p{margin:14px auto 0;width:520px;font-size:16px;line-height:26px;text-transform:uppercase;letter-spacing:.5px}
.btn{display:inline-block;background:var(--green);color:var(--white);font-weight:700;font-size:15px;padding:14px 28px;text-transform:uppercase}
.hero-box .btn{margin-top:26px}
.hero-curve{position:absolute;left:0;bottom:0;width:1200px;height:180px}

/* section titles */
.section-title{text-align:center;font-size:38px;font-weight:700;text-transform:uppercase;color:var(--ink)}
.section-title span{color:var(--green)}
.title-rule{width:90px;height:3px;background:var(--green);margin:16px auto 0}

/* preservation */
.preservation{top:940px;height:540px}
.preservation .section-title{margin-top:30px}
.ring-row{position:absolute;left:170px;top:180px;width:860px;height:300px}
.ring-link{position:absolute;left:140px;top:130px;width:580px;height:40px;background:var(--green-dark)}
.ring{position:absolute;top:0;width:300px;height:300px;border-radius:50%;background:var(--green-light);padding:16px}
.ring-inner{width:100%;height:100%;border-radius:50%;background:var(--green);color:var(--white);text-align:center;padding-top:40px}
.ring-inner h3{margin-top:14px;font-size:17px;font-weight:700;line-height:22px;text-transform:uppercase}
.ring-inner .btn-outline{display:inline-block;margin-top:18px;border:2px solid var(--white);font-size:12px;font-weight:700;padding:7px 16px}
.ring:nth-of-type(2){left:0}
.ring:nth-of-type(3){left:280px}
.ring:nth-of-type(4){left:560px}

/* intro */
.intro{top:1480px;height:540px;background:var(--band)}
.intro-shot{position:absolute;left:100px;top:90px;width:520px;height:340px;border-radius:14px 14px 0 0;background:#222;padding:16px}
.intro-shot-screen{width:100%;height:100%;background:linear-gradient(135deg,#f4f6f2,#c9d9bd 55%,#e9eadf)}
.intro-base{position:absolute;left:60px;top:430px;width:600px;height:22px;border-radius:0 0 14px 14px;background:#bdbdbd}
.intro-badge{position:absolute;left:560px;top:110px;width:110px;height:110px;border-radius:50%;background:#3a4a7a}
.intro-copy{position:absolute;left:700px;top:90px;width:420px}
.intro-copy h2{font-size:32px;font-weight:700;text-transform:uppercase}
.intro-copy h2 span{color:var(--green)}
.intro-copy p{margin-top:18px;font-size:15px;line-height:24px;color:var(--muted)}
.tick-list{margin-top:22px}
.tick-list li{display:flex;align-items:center;gap:12px;font-size:15px;color:var(--ink);margin-bottom:16px}

/* perfect for */
.perfect{top:2020px;height:740px}
.perfect .section-title{margin-top:80px}
.card-row{position:absolute;left:114px;top:200px;display:flex;gap:48px}
.card{width:292px}
.card-media{position:relative;width:292px;height:210px}
.card-media .play{position:absolute;left:116px;top:75px;width:60px;height:60px;border-radius:50%;background:rgba(40,40,40,.85);display:flex;align-items:center;justify-content:center}
.card h3{margin-top:26px;text-align:center;font-size:19px;font-weight:700;text-transform:uppercase}
.card ul{margin-top:20px}
.card li{display:flex;align-items:flex-start;gap:10px;font-size:14px;line-height:20px;color:var(--muted);margin-bottom:14px}
.card li svg{flex:none;margin-top:3px}

/* clients */
.clients{top:2760px;height:560px;background:linear-gradient(90deg,#3f9b2c,#5bb23d)}
.clients .section-title{margin-top:60px;color:var(--white)}
.clients .title-rule{background:var(--white)}
.testimonial-row{position:absolute;left:114px;top:200px;display:flex;gap:48px}
.testimonial{width:292px;text-align:center;color:var(--white)}
.avatar{width:140px;height:140px;border-radius:50%;margin:0 auto;border:5px solid var(--white);background:linear-gradient(160deg,#d9d4cc,#8d8a84)}
.testimonial p{margin-top:26px;font-size:14px;line-height:22px}
.testimonial h4{margin-top:18px;font-size:17px;font-weight:700;text-transform:uppercase}
.testimonial small{display:block;margin-top:4px;font-size:13px}

/* cta */
.cta{top:3320px;height:240px;text-align:center}
.cta h2{margin-top:46px;font-size:34px;font-weight:700;line-height:44px;text-transform:uppercase}
.cta h2 span{color:var(--green)}
.cta-actions{margin-top:26px;display:flex;justify-content:center;gap:16px}
.cta-actions .btn.dark{background:var(--ink)}

/* footer */
.site-footer{top:3560px;height:304px;background:var(--footer);color:#cfcfcf}
.footer-cols{position:absolute;left:130px;top:42px;display:flex;gap:40px}
.footer-col{width:220px}
.footer-col h5{font-size:16px;font-weight:700;color:var(--white);text-transform:uppercase;margin-bottom:18px}
.footer-col li{font-size:14px;margin-bottom:10px}
.footer-col p{font-size:14px;line-height:20px}
.email-field{margin-top:16px;width:240px;height:40px;background:var(--white);color:#888;font-size:13px;display:flex;align-items:center;justify-content:space-between;padding:0 12px}
.footer-bar{position:absolute;left:0;bottom:0;width:1200px;height:52px;background:var(--footer-bar);text-align:center;font-size:13px;line-height:52px;color:#bbb}
</style>
</head>
<body>

<header class="site-header">
  <div class="brand">
    <div class="brand-mark"></div>
    <div class="brand-name">FERN LATTICE</div>
  </div>
  <div class="call-pill">
    <span class="call-icon">
      <svg width="22" height="22" viewBox="0 0 24 24"><path fill="#fff" d="M6.6 10.8a15 15 0 0 0 6.6 6.6l2.2-2.2c.3-.3.7-.4 1-.2 1.1.4 2.3.6 3.6.6.6 0 1 .4 1 1V20c0 .6-.4 1-1 1C10.6 21 3 13.4 3 4c0-.6.4-1 1-1h3.5c.6 0 1 .4 1 1 0 1.3.2 2.5.6 3.6.1.3 0 .7-.2 1z"/></svg>
    </span>
    CALL US : 000-555-0147
  </div>
  <nav class="main-nav">
    <span class="active">HOME</span>
    <span>FERN LATTICE</span>
    <span>OUR SPROUT ORACLE</span>
    <span>PRODUCTS</span>
    <span>TUTORIAL</span>
    <span>CONTACT US</span>
  </nav>
</header>

<section class="hero">
  <div class="hero-art" role="img" aria-label="Hand drawing a colored landscape site plan with trees and pathways"></div>
  <div class="hero-box">
    <h1>FERN LATTICE</h1>
    <p>Predict which trees survive construction and plan every root zone before ground breaks</p>
    <span class="btn">Read More</span>
  </div>
  <svg class="hero-curve" viewBox="0 0 1200 180" preserveAspectRatio="none">
    <path d="M0 60 C300 170 800 180 1200 40 L1200 180 L0 180 Z" fill="#2b7a1d"/>
    <path d="M0 90 C300 190 800 200 1200 80 L1200 180 L0 180 Z" fill="#ffffff"/>
  </svg>
</section>

<section class="preservation">
  <h2 class="section-title">Tree Preservation <span>Reinvented</span></h2>
  <div class="title-rule"></div>
  <div class="ring-row">
    <div class="ring-link"></div>
    <div class="ring">
      <div class="ring-inner">
        <svg width="60" height="60" viewBox="0 0 60 60"><circle cx="30" cy="30" r="26" fill="none" stroke="#fff" stroke-width="3"/><path d="M30 10 L36 30 L30 50 L24 30 Z" fill="#fff"/><circle cx="30" cy="30" r="4" fill="#3d9a2c"/></svg>
        <h3>Multifactor<br>Survival Analysis</h3>
        <span class="btn-outline">READ MORE</span>
      </div>
    </div>
    <div class="ring">
      <div class="ring-inner">
        <svg width="60" height="60" viewBox="0 0 60 60"><rect x="6" y="24" width="30" height="16" rx="3" fill="#fff"/><rect x="34" y="28" width="22" height="8" rx="4" fill="none" stroke="#fff" stroke-width="3"/><rect x="12" y="16" width="14" height="8" fill="none" stroke="#fff" stroke-width="3"/></svg>
        <h3>Arborist<br>Designed</h3>
        <span class="btn-outline">READ MORE</span>
      </div>
    </div>
    <div class="ring">
      <div class="ring-inner">
        <svg width="60" height="60" viewBox="0 0 60 60"><path d="M18 8 L18 46 L28 37 L35 52 L41 49 L34 34 L47 34 Z" fill="#fff"/></svg>
        <h3>Point and<br>Click Base</h3>
        <span class="btn-outline">READ MORE</span>
      </div>
    </div>
  </div>
</section>

<section class="intro">
  <div class="intro-shot"><div class="intro-shot-screen" role="img" aria-label="Screenshot of the Fern Lattice planning dashboard on a laptop"></div></div>
  <div class="intro-base"></div>
  <div class="intro-badge"></div>
  <div class="intro-copy">
    <h2>Introducing <span>Fern Lattice</span></h2>
    <p>Fern Lattice is a web application built by arborists to forecast tree survival during construction. It lets you weigh cost against the value of every tree on site and keep the ones that matter most.</p>
    <ul class="tick-list">
      <li><svg width="16" height="16" viewBox="0 0 16 16"><path d="M2 8l4 4 8-9" fill="none" stroke="#3d9a2c" stroke-width="2.5"/></svg>Accurately Predict Tree Survival</li>
      <li><svg width="16" height="16" viewBox="0 0 16 16"><path d="M2 8l4 4 8-9" fill="none" stroke="#3d9a2c" stroke-width="2.5"/></svg>Use Existing PDF Site Plans</li>
      <li><svg width="16" height="16" viewBox="0 0 16 16"><path d="M2 8l4 4 8-9" fill="none" stroke="#3d9a2c" stroke-width="2.5"/></svg>Multi-Factor Arborist-Designed Survival Algorithm</li>
      <li><svg width="16" height="16" viewBox="0 0 16 16"><path d="M2 8l4 4 8-9" fill="none" stroke="#3d9a2c" stroke-width="2.5"/></svg>Adjust Plans For Best Survivability</li>
      <li><svg width="16" height="16" viewBox="0 0 16 16"><path d="M2 8l4 4 8-9" fill="none" stroke="#3d9a2c" stroke-width="2.5"/></svg>Print Certified Reports For Clients</li>
    </ul>
  </div>
</section>

<section class="perfect">
  <h2 class="section-title">Fern Lattice <span>Is Perfect For</span></h2>
  <div class="title-rule"></div>
  <div class="card-row">
    <article class="card">
      <div class="card-media" role="img" aria-label="Video thumbnail of municipal planners reviewing a site map" style="background:linear-gradient(135deg,#e8e2d8,#c9b9a4)">
        <span class="play"><svg width="20" height="20" viewBox="0 0 20 20"><path d="M5 3l12 7-12 7z" fill="#fff"/></svg></span>
      </div>
      <h3>Municipal Planners</h3>
      <ul>
        <li><svg width="12" height="12" viewBox="0 0 12 12"><path d="M1 6l3 3 7-7" fill="none" stroke="#3d9a2c" stroke-width="2"/></svg>Numerically assess viability of tree plans</li>
        <li><svg width="12" height="12" viewBox="0 0 12 12"><path d="M1 6l3 3 7-7" fill="none" stroke="#3d9a2c" stroke-width="2"/></svg>Simulate plan changes to increase survivability</li>
        <li><svg width="12" height="12" viewBox="0 0 12 12"><path d="M1 6l3 3 7-7" fill="none" stroke="#3d9a2c" stroke-width="2"/></svg>Arborist expertise at a fraction of the price</li>
        <li><svg width="12" height="12" viewBox="0 0 12 12"><path d="M1 6l3 3 7-7" fill="none" stroke="#3d9a2c" stroke-width="2"/></svg>Enterprise pricing</li>
      </ul>
    </article>
    <article class="card">
      <div class="card-media" role="img" aria-label="Video thumbnail of builders studying blueprints on site" style="background:linear-gradient(135deg,#d8dde2,#a7b2bb)">
        <span class="play"><svg width="20" height="20" viewBox="0 0 20 20"><path d="M5 3l12 7-12 7z" fill="#fff"/></svg></span>
      </div>
      <h3>Builders &amp; Developers</h3>
      <ul>
        <li><svg width="12" height="12" viewBox="0 0 12 12"><path d="M1 6l3 3 7-7" fill="none" stroke="#3d9a2c" stroke-width="2"/></svg>Stay ahead of local tree preservation rules</li>
        <li><svg width="12" height="12" viewBox="0 0 12 12"><path d="M1 6l3 3 7-7" fill="none" stroke="#3d9a2c" stroke-width="2"/></svg>Be proactive on tree preservation planning</li>
        <li><svg width="12" height="12" viewBox="0 0 12 12"><path d="M1 6l3 3 7-7" fill="none" stroke="#3d9a2c" stroke-width="2"/></svg>Preserve the most valuable trees</li>
        <li><svg width="12" height="12" viewBox="0 0 12 12"><path d="M1 6l3 3 7-7" fill="none" stroke="#3d9a2c" stroke-width="2"/></svg>Advertise your projects as tree-friendly</li>
      </ul>
    </article>
    <article class="card">
      <div class="card-media" role="img" aria-label="Video thumbnail of a forest path in a landscaped park" style="background:linear-gradient(135deg,#6f8f4a,#2f4a22)">
        <span class="play"><svg width="20" height="20" viewBox="0 0 20 20"><path d="M5 3l12 7-12 7z" fill="#fff"/></svg></span>
      </div>
      <h3>Landscape Architects</h3>
      <ul>
        <li><svg width="12" height="12" viewBox="0 0 12 12"><path d="M1 6l3 3 7-7" fill="none" stroke="#3d9a2c" stroke-width="2"/></svg>Exit the role of rule-of-thumb calculations</li>
        <li><svg width="12" height="12" viewBox="0 0 12 12"><path d="M1 6l3 3 7-7" fill="none" stroke="#3d9a2c" stroke-width="2"/></svg>Provide tree survival alternatives to clients</li>
        <li><svg width="12" height="12" viewBox="0 0 12 12"><path d="M1 6l3 3 7-7" fill="none" stroke="#3d9a2c" stroke-width="2"/></svg>Don't waste time and money on trees</li>
        <li><svg width="12" height="12" viewBox="0 0 12 12"><path d="M1 6l3 3 7-7" fill="none" stroke="#3d9a2c" stroke-width="2"/></svg>Arborist expertise at your fingertips</li>
      </ul>
    </article>
  </div>
</section>

<section class="clients">
  <h2 class="section-title">Fern Lattice Clients</h2>
  <div class="title-rule"></div>
  <div class="testimonial-row">
    <div class="testimonial">
      <div class="avatar" role="img" aria-label="Portrait photo of a client"></div>
      <p>Fern Lattice helped our team weigh the future of the trees on our site. The report was clear and made the approval easy.</p>
      <h4>Marco Ellery</h4>
      <small>Municipal Planner</small>
    </div>
    <div class="testimonial">
      <div class="avatar" role="img" aria-label="Portrait photo of a client"></div>
      <p>We saved money by spotting plan changes early. One small shift kept dozens of mature trees and sped up the permit.</p>
      <h4>Dean Holloway</h4>
      <small>Site Development Lead</small>
    </div>
    <div class="testimonial">
      <div class="avatar" role="img" aria-label="Portrait photo of a client"></div>
      <p>Having Fern Lattice on our projects lets us show clients how each tree will fare and which choices protect them best.</p>
      <h4>Tessa Brandt</h4>
      <small>Landscape Architect</small>
    </div>
  </div>
</section>

<section class="cta">
  <h2>Improve Your Tree<br><span>Preservation Planning Today</span></h2>
  <div class="cta-actions">
    <span class="btn">Fern Lattice</span>
    <span class="btn dark">Sprout Oracle</span>
  </div>
</section>

<footer class="site-footer">
  <div class="footer-cols">
    <div class="footer-col">
      <h5>Information</h5>
      <ul>
        <li>Sitemap</li>
        <li>How Fern Lattice Works</li>
        <li>Fern Lattice Sprout Oracle</li>
        <li>Fern Lattice Mission and Team</li>
        <li>The Fern Lattice Algorithm</li>
        <li>Contact Us</li>
      </ul>
    </div>
    <div class="footer-col">
      <h5>Customer Service</h5>
      <ul>
        <li>Privacy notice</li>
        <li>Conditions of Use</li>
      </ul>
    </div>
    <div class="footer-col">
      <h5>My Account</h5>
      <ul>
        <li>My account</li>
        <li>Orders</li>
        <li>Shopping cart</li>
      </ul>
    </div>
    <div class="footer-col">
      <h5>Newsletter</h5>
      <p>Get our latest tree news by email</p>
      <div class="email-field">Enter your Email
        <svg width="14" height="14" viewBox="0 0 14 14"><path d="M1 7h11M8 3l4 4-4 4" fill="none" stroke="#3d9a2c" stroke-width="2"/></svg>
      </div>
    </div>
  </div>
  <div class="footer-bar">© Copyright 2021 Fern Lattice. All rights reserved.</div>
</footer>

</body>
</html>
```